Coffee bag stamp design for new coffee brand

Stamp design that will be used like a label on a coffee package.
It must be a vector that can be produced as a stamp. Coffee bag is from brown craft paper. I upload image of this bag. Size of design is 80mm x 140mm.
I also uploaded two pictures for inspiration, but I will also appreciate new ideas.

Target Market(s)

Coffee lovers, who love to try new coffee. Also hipsters.

Colors

Designer to choose only greyscale colors for use in the design.

Requirements
Must have
• Some information about coffee must have:
Name: BRAZIL (the biggest font in that design)
Region: Santos
Altitude: 60 – 1200 m.n.m.
Variety: Arabica
Processing: unwashed

```html
<!DOCTYPE html>
<html lang="en">
<head>
<meta charset="utf-8">
<title>Brazil Arabica – Coffee Bag Stamp</title>
<link rel="stylesheet" href="https://fonts.googleapis.com/css2?family=Playfair+Display:wght@600&family=Oswald:wght@500;600;700&family=Cinzel:wght@500&display=swap">
<style>
  :root {
    --kraft: #d3b59b;
    --ink: #111111;
    --art-tone: #b39a84;
  }
  html, body {
    margin: 0;
    padding: 0;
    overflow: hidden;
  }
  .stamp {
    position: relative;
    width: 704px;
    height: 1200px;
    background: var(--kraft);
    overflow: hidden;
  }
  .hero-art {
    position: absolute;
    left: 112px;
    top: 133px;
    width: 491px;
    height: 380px;
    background: radial-gradient(ellipse at 50% 55%, #9f8773 0%, var(--art-tone) 55%, var(--kraft) 100%);
  }
  .origin-name {
    position: absolute;
    left: 0;
    top: 520px;
    width: 704px;
    height: 170px;
  }
  .origin-name text {
    font-family: "Playfair Display", "Bodoni Moda", serif;
    font-weight: 600;
    fill: var(--ink);
  }
  .variety-row {
    position: absolute;
    left: 115px;
    top: 698px;
    width: 474px;
    height: 34px;
  }
  .variety-rule {
    position: absolute;
    top: 6px;
    width: 92px;
    height: 22px;
    background: repeating-linear-gradient(to bottom, var(--ink) 0 3px, transparent 3px 6.4px);
  }
  .variety-rule.left { left: 0; }
  .variety-rule.right { right: 0; width: 76px; }
  .variety-label {
    position: absolute;
    left: 98px;
    right: 82px;
    top: 0;
    text-align: center;
    font-family: "Oswald", "Arial Narrow", sans-serif;
    font-weight: 600;
    font-size: 30px;
    line-height: 34px;
    letter-spacing: 15px;
    padding-left: 15px;
    color: var(--ink);
  }
  .top-rule {
    position: absolute;
    left: 115px;
    top: 768px;
    width: 471px;
    height: 5px;
    background: var(--ink);
  }
  .region-band {
    position: absolute;
    left: 115px;
    top: 781px;
    width: 471px;
    height: 68px;
    background: var(--ink);
    color: var(--kraft);
    font-family: "Cinzel", "Trajan Pro", serif;
    font-weight: 500;
    font-size: 40px;
    line-height: 68px;
    letter-spacing: 12px;
    padding-left: 12px;
    box-sizing: border-box;
    text-align: center;
  }
  .spec-table {
    position: absolute;
    left: 115px;
    top: 858px;
    width: 471px;
    height: 185px;
    border: 3px solid var(--ink);
    box-sizing: border-box;
  }
  .brand-cell {
    position: absolute;
    left: 0;
    top: 0;
    width: 193px;
    height: 179px;
    border-right: 3px solid var(--ink);
    display: flex;
    align-items: center;
    justify-content: center;
    gap: 8px;
  }
  .brand-dot {
    width: 14px;
    height: 14px;
    border-radius: 50%;
    background: var(--ink);
    flex: none;
  }
  .brand-name {
    font-family: "Oswald", "Arial Narrow", sans-serif;
    font-weight: 600;
    font-size: 22px;
    line-height: 1;
    color: var(--ink);
    text-transform: uppercase;
  }
  .spec {
    position: absolute;
    left: 196px;
    width: 269px;
    display: flex;
    align-items: center;
    justify-content: center;
    font-family: "Oswald", "Arial Narrow", sans-serif;
    color: var(--ink);
  }
  .spec.altitude {
    top: 0;
    height: 81px;
    border-bottom: 3px solid var(--ink);
    font-weight: 600;
    font-size: 30px;
  }
  .spec.process {
    top: 84px;
    height: 95px;
    font-weight: 600;
    font-size: 46px;
  }
</style>
</head>
<body>
<main class="stamp">
  <div class="hero-art" role="img" aria-label="Line-art illustration of a woman with flowers in her curly hair holding up a coffee bean, framed by a sunburst, waves, palm leaves and ornate corner flourishes"></div>

  <svg class="origin-name" viewBox="0 0 704 170" aria-label="Brazil">
    <text x="115" y="146" font-size="188" textLength="474" lengthAdjust="spacingAndGlyphs">Brazil</text>
  </svg>

  <div class="variety-row">
    <span class="variety-rule left"></span>
    <span class="variety-label">ARABICA</span>
    <span class="variety-rule right"></span>
  </div>

  <div class="top-rule"></div>
  <div class="region-band">SANTOS</div>

  <section class="spec-table">
    <div class="brand-cell">
      <span class="brand-dot"></span>
      <span class="brand-name">Kavana Coffee</span>
    </div>
    <div class="spec altitude">60 - 1200 M.N.M.</div>
    <div class="spec process">UNWASHED</div>
  </section>
</main>
</body>
</html>
```